Awesome Dessert Baker needs Sticker Design

My wife is an incredible baker. She specializes in desserts and everyone that tastes her baked goods has told her to start selling them. She recently decided to go into business and just through word of mouth and her reputation she is already getting steady orders.

She is looking to have a sticker developed to put on her cake boxes and packaging.

She wants the following:
1. Colors to be used- hot pink, purple, white
2. Want a sleek, modern design and style incorporating following:
name: Whisked by Nora
tel: 646 382 1074
email: nora@whiskedbynora.example

**no old fashion baking references like rolling pins, aprons, ect.

We want the sticker to be very appealing and eye catching that will further promote her image and business.

Industry/Entity Type

Fashion

Requirements
Must have
• Must contain the following information:

Whisked by Nora
646 382 1074 (please make small and discreet)
nora@whiskedbynora.example (please make small and discreet)
Should not have
• **no old fashion baking references like rolling pins, aprons, ect.

```html
<!DOCTYPE html>
<html lang="en">
<head>
<meta charset="utf-8">
<title>Whisked by Nora — Packaging Sticker</title>
<link rel="stylesheet" href="https://fonts.googleapis.com/css2?family=Felipa&display=swap">
<style>
  :root {
    --cream: #f0dbae;
    --hot-pink: #ec2a7d;
    --purple: #6b2263;
    --crimson: #b8184a;
    --white: #ffffff;
  }
  html, body {
    margin: 0;
    padding: 0;
    width: 1200px;
    height: 900px;
    overflow: hidden;
    background: var(--cream);
  }
  .sticker-canvas {
    position: relative;
    width: 1200px;
    height: 900px;
    background: var(--cream);
  }
  .sticker-shape {
    position: absolute;
    inset: 0;
  }
  .sticker-text {
    position: absolute;
    left: 0;
    width: 1200px;
    text-align: center;
    color: var(--white);
    font-family: "Felipa", cursive;
    margin: 0;
  }
  .brand-name {
    top: 398px;
    left: 8px;
    font-size: 62px;
    font-weight: 400;
    line-height: 1;
  }
  .contact {
    top: 535px;
    left: 4px;
    font-size: 28px;
    line-height: 44px;
  }
  .contact span { display: block; }
</style>
</head>
<body>
<main class="sticker-canvas">
  <svg class="sticker-shape" width="1200" height="900" viewBox="0 0 1200 900" aria-hidden="true">
    <circle class="outer-ring" cx="600" cy="450" r="427" fill="var(--hot-pink)"/>
    <circle class="purple-band" cx="600" cy="450" r="413" fill="var(--purple)"/>
    <g class="scalloped-center" fill="var(--crimson)" stroke="var(--crimson)">
      <circle cx="600" cy="452" r="332"/>
      <circle cx="600" cy="452" r="334" fill="none" stroke-width="34" stroke-linecap="round" stroke-dasharray="0 68"/>
      <circle cx="600" cy="452" r="330" fill="none" stroke-width="40" stroke-linecap="round" stroke-dasharray="0 97" stroke-dashoffset="30"/>
    </g>
  </svg>

  <h1 class="sticker-text brand-name">Whisked by Nora</h1>
  <p class="sticker-text contact">
    <span class="contact-email">Email: nora@whiskedbynora.example</span>
    <span class="contact-tel">Tel: 646 382 1074</span>
  </p>
</main>
</body>
</html>
```